Group training gym/bootcamp needs a web design

We need a website for our gym that is based in Sydney. We have indoor functional training classes and outdoor bootcamp classes. We would like the web site to have a video (to be created) and photo gallery. I would like the site made on word press and i would like to be able to make minor changes such as changing images and text without having to use a designer.

The website should have the following pages: home page; the gym; the bootcamp; photo gallery; about us; contact.

I have uploaded our logo and i would like to keep to these colour (blue,yellow,silver) and black is also allowed

Target Market(s)

18-50 male and female

Industry/Entity Type

Gym

Coding

Coded - Design and coding required

Number of Pages Required

5+ page

Font styles to use
Sans Serif

Colors
0692cd
fbed22
1b1b1b
e8e8e8

Requirements
Must have
• The website should have the following pages: home page; the gym; the bootcamp; photo gallery; about us; contact.
• I have uploaded our logo and i would like to keep to these colour (blue,yellow,silver) and black is also allowed
• Video upload and photo upload

```html
<!DOCTYPE html>
<html lang="en">
<head>
<meta charset="utf-8">
<title>Ironline Fitness – Contact Us</title>
<link href="https://fonts.googleapis.com/css2?family=Montserrat:wght@400;600;700;800&family=Open+Sans:wght@400;600;700&display=swap" rel="stylesheet">
<style>
:root{
  --blue:#0692cd;
  --blue-soft:#4fb3e0;
  --yellow:#fbed22;
  --black:#1b1b1b;
  --silver:#e8e8e8;
  --grey-text:#777;
  --line:#dcdcdc;
  --white:#fff;
}
*{box-sizing:border-box;margin:0;padding:0}
html,body{width:882px;height:1200px;overflow:hidden;background:var(--white)}
body{font-family:"Open Sans",Arial,sans-serif;color:#555;position:relative}
.page{position:relative;width:882px;height:1200px}

/* hero */
.hero{position:absolute;left:0;top:0;width:882px;height:310px;
  background:linear-gradient(180deg,#1c1d1f 0%,#4a4a44 30%,#6b6a55 55%,#5f7146 80%,#3f5430 100%)}
.hero-shade{position:absolute;left:0;top:0;width:882px;height:70px;background:linear-gradient(180deg,rgba(0,0,0,.75),rgba(0,0,0,0))}
.main-nav{position:absolute;top:0;left:0;width:882px;height:70px}
.main-nav a{position:absolute;top:18px;font:600 11px "Montserrat",sans-serif;color:var(--white);text-decoration:none;text-transform:uppercase;letter-spacing:.3px}
.main-nav a.active{color:var(--yellow)}
.brand-top{position:absolute;left:341px;top:10px;width:200px;text-align:center}
.brand-top .mark{display:block;width:44px;height:44px;border-radius:50%;background:var(--blue);border:3px solid var(--yellow);margin:0 auto 4px}
.brand-top .name{font:700 11px "Montserrat",sans-serif;color:var(--white);letter-spacing:1px}

/* contact heading */
.contact-head{position:absolute;top:405px;left:0;width:882px;text-align:center}
.contact-head .mark{display:block;width:30px;height:30px;border-radius:50%;background:var(--blue);margin:0 auto 2px}
.contact-head .name{font:700 8px "Montserrat",sans-serif;color:var(--blue);letter-spacing:.8px}
.contact-head h1{font:800 24px "Montserrat",sans-serif;color:var(--blue);margin-top:10px;letter-spacing:.5px}
.contact-head p{width:620px;margin:14px auto 0;font-size:11px;line-height:19px;color:var(--grey-text)}

/* form */
.contact-form{position:absolute;left:53px;top:577px;width:388px}
.field{display:block;height:27px;border:1px solid var(--line);border-radius:2px;margin-bottom:12px;padding:0 9px;font-size:10px;line-height:25px;color:#999;background:var(--white)}
.row{display:flex;gap:12px}
.row .field{flex:1}
.field.area{height:68px}
.submit{position:absolute;left:257px;top:300px;width:82px;height:30px;border-radius:16px;background:var(--yellow);font:700 11px "Montserrat",sans-serif;color:var(--black);text-align:center;line-height:30px}

/* info */
.contact-info{position:absolute;left:500px;top:577px;width:340px}
.info-item{display:flex;align-items:center;height:30px;margin-bottom:16px;font-size:11px}
.info-item .ico{width:26px;height:26px;border-radius:50%;background:var(--blue-soft);margin-right:12px;display:flex;align-items:center;justify-content:center}
.info-item .label{color:var(--blue-soft);margin-right:6px}
.info-item strong{color:#333;font-weight:700}
.connect{position:absolute;left:0;top:145px;font:700 12px "Montserrat",sans-serif;color:#333}
.socials{position:absolute;left:0;top:172px;display:flex;gap:8px}
.socials span{width:26px;height:26px;border-radius:50%;background:var(--blue)}
.ticks{position:absolute;left:0;top:222px;list-style:none}
.ticks li{display:flex;align-items:center;font-size:9px;color:#999;height:20px}
.ticks li i{width:11px;height:11px;border:1px solid #bbb;margin-right:9px;display:flex;align-items:center;justify-content:center}

/* newsletter band */
.band{position:absolute;left:0;top:985px;width:882px;height:73px;background:var(--blue)}
.band .title{position:absolute;left:53px;top:28px;font:700 12px "Montserrat",sans-serif;color:var(--white);letter-spacing:.5px}
.news-input{position:absolute;left:143px;top:22px;width:195px;height:28px;border-radius:14px;background:var(--white);font-size:9px;color:#999;line-height:28px;padding-left:12px}
.news-input b{position:absolute;right:2px;top:2px;width:34px;height:24px;border-radius:12px;background:var(--yellow);font:700 9px "Montserrat",sans-serif;color:var(--black);text-align:center;line-height:24px}
.brand-band{position:absolute;left:371px;top:-22px;width:140px;text-align:center}
.brand-band .mark{display:block;width:50px;height:50px;border-radius:50%;background:var(--blue);border:3px solid var(--yellow);margin:0 auto 4px}
.brand-band .name{font:700 10px "Montserrat",sans-serif;color:var(--white);letter-spacing:1px}
.follow{position:absolute;left:583px;top:28px;font:700 12px "Montserrat",sans-serif;color:var(--white);letter-spacing:.5px}
.follow-icons{position:absolute;left:670px;top:25px;display:flex;gap:14px}
.follow-icons span{width:18px;height:18px;border-radius:50%;background:var(--white)}

/* footer */
.footer{position:absolute;left:0;top:1058px;width:882px;height:142px;background:var(--black);text-align:center}
.footer-nav{margin-top:36px;display:flex;justify-content:center;gap:40px}
.footer-nav a{font:600 11px "Open Sans",sans-serif;color:var(--white);text-decoration:none}
.footer p{font-size:8px;color:#888;margin-top:14px}
.footer p + p{margin-top:5px}
</style>
</head>
<body>
<div class="page">

  <header class="hero" role="img" aria-label="Photo of a group bootcamp class doing push-ups and kettlebell exercises outdoors"></header>
  <div class="hero-shade"></div>
  <nav class="main-nav">
    <a href="#" style="left:97px">Home</a>
    <a href="#" style="left:163px">The Gym</a>
    <a href="#" style="left:248px">The Bootcamp</a>
    <a href="#" style="left:548px">Gallery</a>
    <a href="#" style="left:617px">About Us</a>
    <a href="#" class="active" style="left:700px">Contact Us</a>
    <div class="brand-top"><span class="mark"></span><span class="name">IRONLINE FITNESS</span></div>
  </nav>

  <section class="contact-head">
    <span class="mark"></span>
    <span class="name">IRONLINE FITNESS</span>
    <h1>CONTACT US</h1>
    <p>Aliquam molestie, mi at imperdiet euismod, dui purus auctor tellus, et interdum lacus lectus et ante. Sed accumsan sollicitudin sapien, sit amet adipiscing turpis gravida ac. In congue, neque ac lobortis volutpat, libero mauris.</p>
  </section>

  <form class="contact-form">
    <div class="field">Name*</div>
    <div class="field">Email Address*</div>
    <div class="row"><div class="field">City*</div><div class="field">State*</div></div>
    <div class="row"><div class="field">Primary Phone*</div><div class="field">Secondary Phone*</div></div>
    <div class="field">Best time to contact?</div>
    <div class="field area">Comments*</div>
    <div class="submit">SUBMIT</div>
  </form>

  <aside class="contact-info">
    <div class="info-item"><span class="ico"><svg width="12" height="12" viewBox="0 0 24 24"><path fill="#fff" d="M6.6 10.8a15 15 0 0 0 6.6 6.6l2.2-2.2c.3-.3.7-.4 1-.2 1.1.4 2.3.6 3.6.6.6 0 1 .4 1 1V20c0 .6-.4 1-1 1A17 17 0 0 1 3 4c0-.6.4-1 1-1h3.5c.6 0 1 .4 1 1 0 1.3.2 2.5.6 3.6.1.3 0 .7-.2 1z"/></svg></span><span class="label">Call us today:</span><strong>555-014-2200</strong></div>
    <div class="info-item"><span class="ico"><svg width="12" height="12" viewBox="0 0 24 24"><path fill="#fff" d="M3 5h18v14H3z"/><path fill="none" stroke="#4fb3e0" stroke-width="2" d="M3 6l9 7 9-7"/></svg></span><span class="label">Email us:</span><strong>info@ironlinefitness.com</strong></div>
    <div class="info-item"><span class="ico"><svg width="12" height="12" viewBox="0 0 24 24"><path fill="#fff" d="M12 2a7 7 0 0 0-7 7c0 5 7 13 7 13s7-8 7-13a7 7 0 0 0-7-7zm0 9.5A2.5 2.5 0 1 1 12 6.5a2.5 2.5 0 0 1 0 5z"/></svg></span><span class="label">Address:</span><strong>Ipsum dolor sit amet, consectetur</strong></div>
    <div class="connect">Connect With Us</div>
    <div class="socials" aria-label="Social links"><span></span><span></span><span></span></div>
    <ul class="ticks">
      <li><i><svg width="8" height="8" viewBox="0 0 10 10"><path d="M1 5l3 3 5-6" fill="none" stroke="#0692cd" stroke-width="1.6"/></svg></i>Sed in suscipit ante vitae curae nisi risus erat.</li>
      <li><i><svg width="8" height="8" viewBox="0 0 10 10"><path d="M1 5l3 3 5-6" fill="none" stroke="#0692cd" stroke-width="1.6"/></svg></i>Imperdiet accumsan dui tristique vestibulum, dolor nec egestas.</li>
      <li><i><svg width="8" height="8" viewBox="0 0 10 10"><path d="M1 5l3 3 5-6" fill="none" stroke="#0692cd" stroke-width="1.6"/></svg></i>Lorem turpis ac purus sit elit vitae lobortis dui.</li>
    </ul>
  </aside>

  <section class="band">
    <div class="title">NEWSLETTER</div>
    <div class="news-input">Enter Email<b>GO</b></div>
    <div class="brand-band"><span class="mark"></span><span class="name">IRONLINE FITNESS</span></div>
    <div class="follow">FOLLOW US</div>
    <div class="follow-icons" aria-label="Social links"><span></span><span></span><span></span><span></span><span></span><span></span></div>
  </section>

  <footer class="footer">
    <nav class="footer-nav">
      <a href="#">Home</a><a href="#">The Gym</a><a href="#">The Bootcamp</a><a href="#">Photo Gallery</a><a href="#">About us</a><a href="#">Contact us</a>
    </nav>
    <p>Copyright © 2015 Company Name. All Rights Reserved</p>
    <p>Terms Of Service &nbsp;·&nbsp; Privacy Policy</p>
  </footer>

</div>
</body>
</html>
```